Integrative Medical Practice Website Redo

I am needing to have our current website redesigned to make it a responsive website to work on smartphones.
Current website
www.brightoakfm.com
Here are several examples of what I am looking for
https://www.corvanhealth.com/
I am wanting a popup for a newsletter signup
Looking for a very professional, clean, simple, minimalist, bold well designed website
Colors would ideally be greens and blues, cool tones, muted colors, or graytones like:
https://journeybright.org/
Several other clean design examples
http://7harborsrenton.com/
http://www.belvomedical.com/
http://sunpathyouth.com/
http://yourcellduke.com/
I would like the top navigation bar to be able to slide down while browsing site
We are also needing to add several features that are not on our current website:
Questionnaire buttons
Are you toxic questionnaire?
Take our hormone quiz to find out if hormones are affecting your health.
online scheduling option for:
nutrition counselling
testing like body composition, basal metabolic rate, CIMT, breast thermography, VO2 Max testing, Vita Trace
Therapies like whole body vibration, infrared sauna, Exercise with oxygen, hyperbaric oxygen, spinal decompression
Need to have separate page for different services and split up services into:
Consults/Office Visits, Testing, Therapies, Procedures
Need to have a button link to patient portal
Needs to have online store
Need to add navigation button "Start Here"
Need a spot for a video on practice summary
Newsletter signup to collect emails
Testimonials from linkpage
Blog that posts can be shared with social media
Password protected patient access that can integrate into crate.net ideally
Modules for programs online classes/videos
I have attached stock images that you can use, but feel free to find others to use.
I have also attached a copy of our current brochure that shows an overview of the practice
Target Market(s)
Health conscious people of all ages looking for a family medicine doctor
Industry/Entity Type
Alternative Medicine
Coding
Coded - Design and coding required
Number of Pages Required
5+ page
Look and feel

```html
<!DOCTYPE html>
<html lang="en">
<head>
<meta charset="utf-8">
<title>Bright Oak Family Medicine – Services</title>
<link rel="stylesheet" href="https://fonts.googleapis.com/css2?family=Lato:wght@300;400&family=Roboto:wght@400;500&display=swap">
<style>
  :root {
    --page-bg: #f7f7f6;
    --title: #3a3c3f;
    --body: #8d9094;
    --accent: #2f75a8;
    --accent-soft: #d9e6ee;
    --leaf: #eef1e4;
  }
  * { box-sizing: border-box; margin: 0; padding: 0; }
  html, body { width: 1200px; height: 1200px; overflow: hidden; }
  body {
    background: var(--page-bg);
    font-family: "Lato", sans-serif;
    position: relative;
  }
  .leaf-decor {
    position: absolute;
    border-radius: 50% 0 50% 0;
    background: radial-gradient(circle at 50% 50%, var(--leaf), rgba(238,241,228,0) 70%);
  }
  .leaf-decor.left { left: 60px; top: 380px; width: 360px; height: 360px; }
  .leaf-decor.right { left: 860px; top: 470px; width: 260px; height: 220px; background: radial-gradient(circle at 50% 50%, #e6eef1, rgba(230,238,241,0) 70%); }
  .service {
    position: absolute;
    width: 420px;
    text-align: center;
  }
  .service .icon { display: block; margin: 0 auto 22px; }
  .service h2 {
    font-family: "Roboto", sans-serif;
    font-weight: 500;
    font-size: 26px;
    color: var(--title);
    margin-bottom: 18px;
  }
  .service p {
    font-size: 15px;
    font-weight: 300;
    line-height: 1.6;
    color: var(--body);
    margin: 0 auto 32px;
    width: 390px;
  }
  .btn {
    display: inline-block;
    width: 160px;
    padding: 16px 0;
    font-size: 15px;
    color: var(--accent);
    border: 1.5px solid var(--accent);
    text-decoration: none;
  }
  .btn.filled { background: var(--accent); color: #fff; }
  .family { left: 90px; top: 120px; }
  .nutrition { left: 650px; top: 170px; }
  .acupuncture { left: 90px; top: 540px; }
  .body-comp { left: 650px; top: 590px; }
</style>
</head>
<body>
  <div class="leaf-decor left" role="img" aria-label="Faint leaf line decoration"></div>
  <div class="leaf-decor right" role="img" aria-label="Faint leaf line decoration"></div>

  <section class="service family">
    <svg class="icon" width="48" height="40" viewBox="0 0 48 40" fill="none" stroke="var(--accent)" stroke-width="2.5">
      <rect x="6" y="12" width="36" height="16" rx="8" transform="rotate(-30 24 20)"/>
      <line x1="20" y1="29" x2="14" y2="15" transform="rotate(-30 24 20) translate(10 -2)"/>
    </svg>
    <h2>Family Medicine</h2>
    <p>In addition to what you would expect from any family medicine clinic, we utilize many different modalities in our attempt to improve your quality of health, whether it is pharmaceutical or nutraceutical.</p>
    <a class="btn" href="#">Read More</a>
  </section>

  <section class="service nutrition">
    <svg class="icon" width="44" height="50" viewBox="0 0 44 50" fill="none" stroke="var(--accent)" stroke-width="2.5">
      <path d="M22 16c-6-5-18-3-18 11 0 10 8 20 13 20 2 0 3-1 5-1s3 1 5 1c5 0 13-10 13-20 0-14-12-16-18-11z"/>
      <path d="M22 16c0-5 2-9 5-11"/>
      <path d="M24 9c3-4 8-4 10-3-2 4-6 5-10 3z"/>
    </svg>
    <h2>Nutrition</h2>
    <p>Having a bachelor's degree in Nutritional Science, Dr. Marsh has the conviction that nutrition is one of the keys to optimal health, since nutrition has an effect on one's body every day.</p>
    <a class="btn filled" href="#">Read More</a>
  </section>

  <section class="service acupuncture">
    <svg class="icon" width="40" height="50" viewBox="0 0 40 50" fill="none" stroke="var(--accent)" stroke-width="2">
      <line x1="8" y1="4" x2="20" y2="46"/>
      <line x1="20" y1="4" x2="22" y2="46"/>
      <line x1="32" y1="4" x2="24" y2="46"/>
      <line x1="14" y1="10" x2="26" y2="46"/>
      <circle cx="8" cy="4" r="2"/><circle cx="20" cy="4" r="2"/><circle cx="32" cy="4" r="2"/>
    </svg>
    <h2>Acupuncture</h2>
    <p>Medical acupuncture provides many types of approaches that are used depending on the individual and their needs, such as pain management, energy balancing, or treating a systemic condition versus local condition.</p>
    <a class="btn" href="#">Read More</a>
  </section>

  <section class="service body-comp">
    <svg class="icon" width="50" height="54" viewBox="0 0 50 54" fill="none" stroke="var(--accent)" stroke-width="2.5" stroke-linejoin="round">
      <path d="M6 50V28c0-6 4-10 10-10h6l2-8c1-5 6-7 10-4l4 3-4 5-4-2-1 8c8-2 16 3 16 13 0 9-7 17-17 17H6z"/>
      <path d="M26 32l-4 7h5l-3 7"/>
    </svg>
    <h2>Body Composition Analysis</h2>
    <p>Corlo's exclusive BIA technology allows this monitor to not only measure weight and body fat, it also provides muscle mass, body water %, basal metabolic rate (BMR), metabolic age, bone mass, visceral fat and rates body physique.</p>
    <a class="btn" href="#">Read More</a>
  </section>
</body>
</html>
```